Building and Construction Business Card Design

We need a business card design for a new building and construction company called "Harbour Stone Dwellings Pty Ltd" We will build any type of building, but our main focus is luxury homes in Sydney.
We would like our business card to be elegant and strong. We have played around with colours and like greys/black and red, but are open to pretty open minded.
Updates

Project Deadline Extended
Reason: Designs are either plain without any wow, or a little comical. Hopefully we can get some designs that are more eye catching, maybe some bling (silver/ gold script) something different please. Thank you for your submissions so far.

Target Market(s)

high end real estate market

Industry/Entity Type

Construction

Contact Information for Business Card

Lachlan Pemberton
Director/Fully Licenced Builder
ABN: 72504918362
m: 0418 735 902
e: info@harbourstonedwellings.com.au
HARBOUR STONE DWELLINGS
website: www.harbourstonedwellings.com.au

Building and Construction

Colors

Designer to choose colors to be used in the design.

Requirements
Nice to have
• The business name "Harbour Stone Dwellings" on one side then all the info on the otherside.

```html
<!DOCTYPE html>
<html lang="en">
<head>
<meta charset="utf-8">
<title>Harbour Stone Dwellings — Business Card</title>
<link href="https://fonts.googleapis.com/css2?family=EB+Garamond:ital,wght@0,600;0,700;1,400;1,500;1,600&display=swap" rel="stylesheet">
<style>
  :root {
    --card-black: #0b0c0d;
    --card-edge: #2a2b2d;
    --gold-muted: #b98a58;
    --gold-warm: #e59f3e;
    --gold-bright: #e8a040;
  }
  html, body {
    margin: 0;
    padding: 0;
    width: 1200px;
    height: 900px;
    overflow: hidden;
    background: var(--card-black);
  }
  .card {
    position: relative;
    width: 1200px;
    height: 900px;
    background:
      radial-gradient(ellipse 95% 95% at 55% 55%, var(--card-black) 70%, var(--card-edge) 100%);
    font-family: "EB Garamond", Garamond, serif;
    line-height: 1;
  }
  .card__person {
    position: absolute;
    right: 88px;
    top: 108px;
    text-align: right;
    color: var(--gold-muted);
    font-style: italic;
  }
  .card__name {
    margin: 0;
    font-size: 50px;
    font-weight: 500;
    letter-spacing: 2px;
  }
  .card__role {
    margin: 14px 0 0;
    font-size: 36px;
    font-weight: 600;
    letter-spacing: 1px;
  }
  .card__company {
    position: absolute;
    left: 84px;
    top: 438px;
    color: var(--gold-warm);
    font-style: italic;
  }
  .card__company-name {
    margin: 0 0 6px;
    font-size: 54px;
    font-weight: 400;
    letter-spacing: 1px;
  }
  .card__detail {
    margin: 0 0 10px 4px;
    font-size: 30px;
    font-weight: 500;
    letter-spacing: 0.5px;
  }
  .card__contact {
    position: absolute;
    left: 80px;
    top: 656px;
    color: var(--gold-bright);
    font-weight: 700;
    font-size: 31px;
  }
  .card__contact p {
    margin: 0 0 10px;
  }
</style>
</head>
<body>
  <main class="card">
    <header class="card__person">
      <h1 class="card__name">Lachlan Pemberton</h1>
      <p class="card__role">Director</p>
    </header>

    <section class="card__company">
      <h2 class="card__company-name">Harbour Stone Dwellings Pty Ltd</h2>
      <p class="card__detail">Fully Licenced Builder</p>
      <p class="card__detail">ABN: 72504918362</p>
      <p class="card__detail">Mobile:&nbsp; 0418 735 902</p>
    </section>

    <section class="card__contact">
      <p class="card__email">eMail: info@harbourstonedwellings.com.au</p>
      <p class="card__web">www.harbourstonedwellings.com.au</p>
    </section>
  </main>
</body>
</html>
```